Website for legal expungement services with button to qualify/disqualify potential clients

Larkfield Record Relief, LLC is a law firm focusing in legal expungement servcies (allowing people to erase criminal court records, police records, proseution files, etc). I want a more modern look which exudes confidence in the services. I am looking for a clean website that looks very polished. I want to keep the pages to a minimum, as I want the page not so much to answer questions, but to direct traffic to contact the law office. I would like the main focus point to be an button which would take a client through a series of questions to see if they would qualify for the services; this serves two purposes 1) to collect contact info for future marketing via email and 2) eliminate individuals who we are currently unable to help. A current theme that I have played around with are "Change so much, you'll need to reintroduce yourself" alongside a picture of a guys hand outstretched.
On the landing page, I would like a very brief and to the point explanation of what the service would be (i.e. "Leave your past in the past; expunge all your criminal records" ), followed by a list of benefits that it provides. (NB: included is a file "law post card-02" that includes the main benefits to expungement). Also included are two logo files for a more updated logo I currently use ("LRR Logo" and LRR Logo2") (NB: I'm open to revisions on this as well). Lastly, I've had two very minor 'ads' that I did ("postcard back" and "HVC Ad") that I like the idea of.

Target Market(s)

Middle/upper-middle class, mostly male, people with a criminal record or criminal accusation

Industry/Entity Type

Legal Services

Coding

Coded - Design and coding required

Requirements
Must have
• Button that attracts attention up front (possibly stand out coloring) to click to open up a series of questions to qualify/eliminate prospects, and simultaneously gather their info. Also, must be mobile friendly.

```html
<!DOCTYPE html>
<html lang="en">
<head>
<meta charset="utf-8">
<title>Larkfield Record Relief, LLC</title>
<link rel="stylesheet" href="https://fonts.googleapis.com/css2?family=Source+Serif+4:wght@400;500&family=Open+Sans:wght@400;600&family=Inter:wght@400;500;600&display=swap">
<style>
:root{
  --stage:#e6e8ec;
  --navy:#0d3576;
  --navy-deep:#0a2350;
  --steel:#2c4b74;
  --accent:#1f5fb0;
  --ink:#1d2a3d;
  --body:#4a5260;
  --white:#ffffff;
  --line:#cfd5de;
  --footer:#1b1c1f;
  --footer-deep:#0f1012;
  --serif:"Source Serif 4", Georgia, serif;
  --sans:"Open Sans", Arial, sans-serif;
  --ui:"Inter", Arial, sans-serif;
}
*{box-sizing:border-box;margin:0;padding:0}
html,body{width:1200px;height:3743px;overflow:hidden;background:var(--stage)}
.page{position:absolute;top:393px;left:0;width:1200px;height:2956px;background:var(--white);overflow:hidden}

/* brand lockup */
.brand{display:flex;align-items:center;color:var(--white);font-family:var(--serif)}
.brand-mark{font-size:40px;letter-spacing:12px;font-weight:400;width:150px}
.brand-rule{width:1px;height:66px;background:currentColor;opacity:.7;margin:0 44px 0 10px}
.brand-name{font-size:23px;line-height:28px;letter-spacing:2px;text-transform:uppercase}

/* hero */
.hero{position:absolute;left:0;top:0;width:1200px;height:631px;background:linear-gradient(100deg,var(--navy-deep) 0%,#0f2f68 45%,#134086 100%)}
.hero .brand{position:absolute;left:87px;top:46px}
.hero-photo{position:absolute;left:642px;top:0;width:558px;height:631px;background:radial-gradient(ellipse at 60% 55%,#1d4f9c 0%,#123777 45%,#0a2350 100%)}
.hero-title{position:absolute;left:87px;top:200px;font-family:var(--serif);font-weight:400;font-size:52px;line-height:61px;color:var(--white)}
.btn-outline{position:absolute;left:87px;top:433px;height:56px;width:344px;border:2px solid var(--white);display:flex;align-items:center;justify-content:center;gap:12px;color:var(--white);font-family:var(--ui);font-weight:500;font-size:19px;letter-spacing:.3px}
.btn-outline::before,.btn-outline::after{content:"";position:absolute;left:8px;right:8px;height:2px;background:var(--white)}
.btn-outline::before{top:-8px}
.btn-outline::after{bottom:-8px}

/* about */
.about{position:absolute;left:0;top:631px;width:1200px;height:447px}
.about-photo{position:absolute;left:87px;top:-29px;width:508px;height:423px;border:3px solid var(--white);background:linear-gradient(135deg,#3b4658 0%,#c9ccd2 45%,#efefef 75%,#b9a27a 100%)}
.about-text{position:absolute;left:628px;top:62px;width:484px}
.eyebrow{font-family:var(--ui);font-size:17px;color:var(--accent);letter-spacing:.3px}
.section-title{font-family:var(--serif);font-weight:400;font-size:33px;color:var(--ink)}
.about-text .section-title{margin-top:8px}
.about-text p{margin-top:22px;font-family:var(--sans);font-size:16px;line-height:26px;color:var(--body);text-align:justify}
.btn-solid{position:relative;display:inline-flex;align-items:center;gap:10px;margin-top:30px;height:46px;padding:0 14px;background:var(--navy);color:var(--white);font-family:var(--ui);font-size:18px;font-weight:500}
.btn-solid::before,.btn-solid::after{content:"";position:absolute;left:4px;right:4px;height:2px;background:var(--navy)}
.btn-solid::before{top:-9px}
.btn-solid::after{bottom:-9px}

/* benefits */
.benefits{position:absolute;left:0;top:1078px;width:1200px;height:500px;background:var(--steel)}
.benefits-title{position:absolute;left:87px;top:52px;font-family:var(--serif);font-weight:400;font-size:44px;line-height:54px;color:var(--white)}
.benefit{position:absolute;width:313px;height:113px;border:1.5px solid rgba(255,255,255,.85);border-radius:6px;display:flex;align-items:center;gap:22px;padding:0 12px;color:var(--white);font-family:var(--ui);font-size:17px;line-height:21px}
.benefit-icon{flex:none;width:96px;height:96px;border-radius:50%;background:var(--white);display:flex;align-items:center;justify-content:center}
.benefit-icon svg{width:52px;height:52px;fill:none;stroke:var(--steel);stroke-width:2;stroke-linecap:round;stroke-linejoin:round}

/* services */
.services{position:absolute;left:0;top:1578px;width:1200px;height:700px}
.services-head{position:absolute;left:0;right:0;top:60px;text-align:center}
.services-head .section-title{margin-top:10px;font-size:34px}
.services-head .rule{width:70px;height:3px;background:var(--accent);margin:18px auto 0}
.service{position:absolute;top:186px;width:322px;height:411px;background:var(--navy);border:2px solid var(--navy)}
.service-photo{height:206px}
.service-box{position:absolute;left:12px;right:12px;top:220px;bottom:12px;border:1.5px solid rgba(255,255,255,.8);text-align:center;color:var(--white);padding-top:20px}
.service-box h3{font-family:var(--serif);font-weight:400;font-size:26px;line-height:32px}
.service-box p{margin:16px auto 0;width:200px;font-family:var(--ui);font-size:11.5px;line-height:16px}

/* footer */
.footer{position:absolute;left:0;top:2590px;width:1200px;height:366px;background:linear-gradient(135deg,var(--footer) 0%,#26272b 50%,var(--footer) 100%)}
.footer .brand{position:absolute;left:0;right:0;top:90px;justify-content:center}
.footer .brand-mark{font-size:36px;width:auto}
.footer .brand-rule{height:78px;margin:0 40px}
.contact{position:absolute;top:198px;left:0;right:0;display:flex;justify-content:center;gap:70px;color:var(--white);font-family:var(--ui)}
.contact-item{display:flex;align-items:center;gap:14px;font-size:15px;line-height:22px}
.contact-item.phone{font-size:22px;font-weight:600}
.contact-item svg{width:32px;height:32px;flex:none}
.copyright{position:absolute;left:0;right:0;bottom:0;height:81px;background:var(--footer-deep);color:#e6e6e6;font-family:var(--ui);font-size:13px;display:flex;align-items:center;justify-content:center}

/* eligibility + faq */
.eligibility{position:absolute;left:175px;top:2245px;width:853px;height:398px;display:flex;background:var(--white);box-shadow:0 6px 24px rgba(0,0,0,.12)}
.form{width:500px;padding:34px 27px 0}
.form .section-title{font-size:30px}
.field{border:1px solid var(--line);height:39px;font-family:var(--ui);font-size:11px;color:#8a919c;padding:0 12px;display:flex;align-items:center;justify-content:space-between;letter-spacing:.3px}
.form-grid{margin-top:22px;display:grid;grid-template-columns:1fr 1fr;gap:11px 22px}
.field.message{grid-column:1/3;height:128px;align-items:flex-start;padding-top:14px}
.send{grid-column:1/3;margin-top:-2px;height:39px;background:var(--navy);color:var(--white);font-family:var(--ui);font-weight:600;font-size:12px;display:flex;align-items:center;justify-content:center;letter-spacing:.3px}
.faq{flex:1;background:var(--navy);margin:2px 2px 2px 0;padding:28px 26px 0;color:var(--white)}
.faq h2{font-family:var(--serif);font-weight:500;font-size:30px;white-space:nowrap}
.faq-item{border-bottom:1px dashed rgba(255,255,255,.5);padding:18px 0 16px;display:flex;justify-content:space-between;align-items:center;font-family:var(--ui);font-weight:600;font-size:13px}
.faq-item svg{width:17px;height:17px;fill:none;stroke:var(--white);stroke-width:1.4}
.faq-open{border-bottom:1px dashed rgba(255,255,255,.5);padding:16px 0 12px}
.faq-open .faq-q{display:flex;justify-content:space-between;align-items:center;font-family:var(--ui);font-weight:600;font-size:13px}
.faq-open p{margin-top:12px;font-family:var(--ui);font-size:10.5px;line-height:15px;opacity:.9}
</style>
</head>
<body>
<main class="page">

  <section class="hero">
    <div class="brand">
      <span class="brand-mark">LRR</span><span class="brand-rule"></span>
      <span class="brand-name">Larkfield Record<br>Relief</span>
    </div>
    <div class="hero-photo" role="img" aria-label="Man in a dark suit holding out an open hand"></div>
    <h1 class="hero-title">Change so much,<br>you'll need to<br>reintroduce yourself</h1>
    <a class="btn-outline">CHECK YOUR QUALIFICATIONS
      <svg width="34" height="14" viewBox="0 0 34 14" fill="none" stroke="#fff" stroke-width="2"><path d="M0 7h32M26 1l6 6-6 6"/></svg></a>
  </section>

  <section class="about">
    <div class="about-photo" role="img" aria-label="Lawyer shaking hands across a desk with scales of justice and a gavel"></div>
    <div class="about-text">
      <div class="eyebrow">ABOUT US</div>
      <h2 class="section-title">Larkfield Record Relief, LLC</h2>
      <p>Larkfield Record Relief is 5-star rated firm, which has been formed with the passing of the New Mexico Expungement law of 2020. It is a subdivision of the Hollis Law Group, and since its creation has helped over 100 New Mexican citizens successfully expunge their criminal records.</p>
      <a class="btn-solid">Read More
        <svg width="32" height="14" viewBox="0 0 32 14" fill="none" stroke="#fff" stroke-width="2"><path d="M0 7h30M24 1l6 6-6 6"/></svg></a>
    </div>
  </section>

  <section class="benefits">
    <h2 class="benefits-title">The Benefit of<br>Expungement</h2>

    <div class="benefit" style="left:444px;top:50px">
      <span class="benefit-icon"><svg viewBox="0 0 52 52"><rect x="12" y="8" width="28" height="18" rx="2"/><circle cx="26" cy="17" r="4"/><path d="M6 36c6-4 12-4 18 0h10c3 0 3 4 0 4H22M6 44l10-2h14l14-10"/></svg></span>
      <span>More and better job opportunities leading to higher income</span>
    </div>
    <div class="benefit" style="left:799px;top:50px">
      <span class="benefit-icon"><svg viewBox="0 0 52 52"><path d="M26 6v24M19 13l7-7 7 7"/><rect x="12" y="22" width="28" height="24"/><path d="M18 30v8M34 30v8"/></svg></span>
      <span>Loan qualification and better loan rates</span>
    </div>
    <div class="benefit" style="left:87px;top:191px">
      <span class="benefit-icon"><svg viewBox="0 0 52 52"><path d="M26 6l16 6v12c0 11-7 18-16 22-9-4-16-11-16-22V12z"/><rect x="20" y="24" width="12" height="10" rx="1"/><path d="M22 24v-4a4 4 0 0 1 8 0v4"/></svg></span>
      <span>Protecting your privacy</span>
    </div>
    <div class="benefit" style="left:444px;top:191px">
      <span class="benefit-icon"><svg viewBox="0 0 52 52"><rect x="10" y="8" width="26" height="36" rx="2"/><path d="M16 16h14M16 22h14M16 28h8M42 14L28 40l-2 6 5-4 14-26z"/></svg></span>
      <span>Better education opportunities</span>
    </div>
    <div class="benefit" style="left:799px;top:191px">
      <span class="benefit-icon"><svg viewBox="0 0 52 52"><path d="M28 8l12 12-6 6-12-12zM25 23L10 38l4 4 15-15M20 46h24"/></svg></span>
      <span>Removing the stigma of having a criminal record</span>
    </div>
    <div class="benefit" style="left:87px;top:331px">
      <span class="benefit-icon"><svg viewBox="0 0 52 52"><path d="M6 24L26 8l20 16M12 20v26h28V20"/><rect x="16" y="28" width="8" height="8"/><rect x="28" y="28" width="8" height="18"/></svg></span>
      <span>More options for housing</span>
    </div>
    <div class="benefit" style="left:444px;top:331px">
      <span class="benefit-icon"><svg viewBox="0 0 52 52"><path d="M16 8h20v10a10 10 0 0 1-20 0zM16 12H9c0 7 4 10 8 10M36 12h7c0 7-4 10-8 10M26 28v10M18 44h16v-6H18z"/></svg></span>
      <span>Qualifying for government assistance programs</span>
    </div>
    <div class="benefit" style="left:799px;top:331px">
      <span class="benefit-icon"><svg viewBox="0 0 52 52"><path d="M12 6h24v20M12 6v40h18"/><path d="M18 14h12M18 20h12M18 26h8"/><circle cx="37" cy="37" r="9"/><path d="M37 32v10M34 35h4a2 2 0 0 1 0 4h-2"/></svg></span>
      <span>Lower insurance premiums</span>
    </div>
  </section>

  <section class="services">
    <div class="services-head">
      <div class="eyebrow">OUR SERVICES</div>
      <h2 class="section-title">Larkfield Record Relief, LLC</h2>
      <div class="rule"></div>
    </div>

    <article class="service" style="left:87px">
      <div class="service-photo" role="img" aria-label="Handcuffs and a gavel on a desk" style="background:linear-gradient(135deg,#e9e9ea 0%,#9da3a9 45%,#5a3a2a 75%,#2a2320 100%)"></div>
      <div class="service-box"><h3>Erase Criminal<br>Court records</h3><p>Lorem Ipsum is simply dummy text of the printing and typesetting industry.</p></div>
    </article>
    <article class="service" style="left:439px">
      <div class="service-photo" role="img" aria-label="Police officers reviewing papers and a tablet" style="background:linear-gradient(135deg,#3a4350 0%,#6e7782 45%,#8a6d4e 70%,#2b2f36 100%)"></div>
      <div class="service-box"><h3>Erase<br>police records</h3><p>Lorem Ipsum is simply dummy text of the printing and typesetting industry.</p></div>
    </article>
    <article class="service" style="left:791px">
      <div class="service-photo" role="img" aria-label="Two lawyers discussing prosecution documents" style="background:linear-gradient(135deg,#1f2a44 0%,#a8242e 35%,#c9ccd2 60%,#1d3a6a 100%)"></div>
      <div class="service-box"><h3>Erase<br>prosecution files</h3><p>Lorem Ipsum is simply dummy text of the printing and typesetting industry.</p></div>
    </article>
  </section>

  <footer class="footer">
    <div class="brand">
      <span class="brand-mark">LRR</span><span class="brand-rule"></span>
      <span class="brand-name">Larkfield Record<br>Relief</span>
    </div>
    <div class="contact">
      <div class="contact-item">
        <svg viewBox="0 0 32 32"><circle cx="16" cy="16" r="15" fill="#fff"/><path d="M16 7a6 6 0 0 0-6 6c0 5 6 12 6 12s6-7 6-12a6 6 0 0 0-6-6z" fill="#1b1c1f"/><circle cx="16" cy="13" r="2.2" fill="#fff"/></svg>
        <span>1480 Alder Ridge Rd Suite 210<br>Larkfield, NM 87020</span>
      </div>
      <div class="contact-item phone">
        <svg viewBox="0 0 32 32"><circle cx="16" cy="16" r="15" fill="#fff"/><path d="M11 8l3 4-2 2c1 3 4 6 7 7l2-2 4 3-2 3c-7 0-14-7-14-14z" fill="#1b1c1f"/></svg>
        <span>505-555-0148</span>
      </div>
      <div class="contact-item">
        <svg viewBox="0 0 32 32"><circle cx="16" cy="16" r="15" fill="#fff"/><rect x="8" y="10" width="16" height="12" rx="1" fill="#1b1c1f"/><path d="M8 11l8 6 8-6" fill="none" stroke="#fff" stroke-width="1.4"/></svg>
        <span>hello@larkfieldrelief.com</span>
      </div>
    </div>
    <div class="copyright">Copyright © 2023 Larkfield Record Relief, LLC | All Right Reserved</div>
  </footer>

  <section class="eligibility">
    <form class="form">
      <h2 class="section-title">Check your Eligebility</h2>
      <div class="form-grid">
        <div class="field">FIRST NAME*</div>
        <div class="field">LAST NAME*</div>
        <div class="field">E-MAIL*</div>
        <div class="field">CASE INVOLVED
          <svg width="12" height="8" viewBox="0 0 12 8" fill="none" stroke="#6b7380" stroke-width="1.5"><path d="M1 1l5 5 5-5"/></svg></div>
        <div class="field message">MESSAGE</div>
        <div class="send">SEND NOW</div>
      </div>
    </form>
    <aside class="faq">
      <h2>Frequently ask Question</h2>
      <div class="faq-item">Lorem Ipsum is simply dummy text<svg viewBox="0 0 17 17"><circle cx="8.5" cy="8.5" r="7.5"/><path d="M5.5 7l3 3 3-3"/></svg></div>
      <div class="faq-item">Lorem Ipsum is simply dummy text<svg viewBox="0 0 17 17"><circle cx="8.5" cy="8.5" r="7.5"/><path d="M5.5 7l3 3 3-3"/></svg></div>
      <div class="faq-item">Lorem Ipsum is simply dummy text<svg viewBox="0 0 17 17"><circle cx="8.5" cy="8.5" r="7.5"/><path d="M5.5 7l3 3 3-3"/></svg></div>
      <div class="faq-open">
        <div class="faq-q">Lorem Ipsum is simply dummy text<svg viewBox="0 0 17 17" width="17" height="17" fill="none" stroke="#fff" stroke-width="1.4"><circle cx="8.5" cy="8.5" r="7.5"/><path d="M5.5 10l3-3 3 3"/></svg></div>
        <p>Lorem Ipsum is simply dummy text of the printing and typesetting industry. Lorem Ipsum has been the industry's standard dummy text ever since the 1500s.</p>
      </div>
    </aside>
  </section>

</main>
</body>
</html>
```